Zielgruppe
Wir sind gerade dabei ein Buch zum Thema 'Konzentrationstraining für Kinder' zu erstellen und brauchen jetzt ein passendes Cover dazu. Bei der Zielgruppe handelt es sich hauptsächlich um Mütter die Lösungen für die Konzentrationsprobleme Ihrer Kinder im Grundschulalter suchen. Die Kinder haben diese Probleme hauptsächlich in der Schule. Das Buch beschreibt hauptsächlich Konzentrationsübungen und -spiele für die Kinder aber auch allgemeine Tipps zur Konzentrationssteigerung wie z.B. Ernährung, Umfeld usw.
Aufgabenstellung
Ein Comic-Stil beim Cover kommt offensichtlich beim Kunden gut an (Konkurrenzanalyse)
Titel, Untertitel und Autorenname müssen auf dem Cover stehen.
Der Titel des Buches lautet: Im stillen Garten - Konzentrationstraining für Kinder in der Praxis: Die 39 besten Übungen für nachhaltig mehr Aufmerksamkeit und Konzentration in der Schule und im Alltag
Autor: Henrike Molldorf
Das Cover wird in 3 verschiedenen Versionen benötigt: Taschenbuch: 5,25 x 8 inch 2. Hardcover: 6 x 9 inch 3. EBook: 2,560 x 1,600 pixel.

```html
<!DOCTYPE html>
<html lang="de">
<head>
<meta charset="utf-8">
<title>Im stillen Garten – Covervarianten</title>
<link href="https://fonts.googleapis.com/css2?family=Fira+Sans+Condensed:wght@500&family=Hind:wght@400;500&family=Fira+Sans:ital,wght@1,400&display=swap" rel="stylesheet">
<style>
  :root {
    --sheet-grey: #b5b5b5;
    --cream: #faf7dc;
    --white: #ffffff;
    --author-grey: #7a7a7a;
    --subtitle-grey: #676767;
    --title-magenta: #c8388f;
    --title-teal: #1a7a80;
    --title-plum: #6b2f6b;
    --tag-grey: #5a5a5a;
    --balloon-orange: #f08a3a;
    --balloon-red: #d8322f;
    --balloon-green: #7cbd45;
    --balloon-blue: #5aa7dc;
    --dress-pink: #c23a9a;
    --wash-light: #f8e3c3;
    --wash-deep: #efc081;
    --cap-brown: #b77a4c;
    --plane-teal: #3fb3b8;
    --sweater-green: #a8c646;
  }
  * { margin: 0; padding: 0; box-sizing: border-box; }
  html, body { width: 853px; height: 1200px; overflow: hidden; }
  body { background: var(--sheet-grey); position: relative; }

  .cover {
    position: absolute;
    width: 415px;
    height: 594px;
    overflow: hidden;
  }
  .cover--balloons { left: 0; top: 0; background: var(--cream); }
  .cover--pilot {
    left: 427px; top: 0;
    background: linear-gradient(160deg, var(--wash-light) 0%, var(--wash-deep) 50%, var(--wash-light) 100%);
  }
  .cover--rainbow { left: 0; top: 606px; background: var(--white); }

  .cover__art { position: absolute; }

  .cover--balloons .cover__art {
    left: 46px; top: 144px; width: 298px; height: 384px;
    border-radius: 150px 150px 24px 24px;
    background: linear-gradient(180deg,
      var(--balloon-blue) 0%,
      var(--balloon-green) 18%,
      var(--balloon-red) 32%,
      var(--balloon-orange) 44%,
      #f3d46a 62%,
      var(--dress-pink) 84%,
      #d98bbf 100%);
    opacity: .85;
  }

  .cover--pilot .cover__art {
    left: 130px; top: 124px; width: 265px; height: 420px;
    border-radius: 130px 130px 30px 30px;
    background: linear-gradient(180deg,
      var(--cap-brown) 0%,
      #e8b596 26%,
      var(--sweater-green) 48%,
      var(--plane-teal) 66%,
      #2f9aa3 84%,
      #9cc2c0 100%);
  }

  .cover--rainbow .cover__art {
    left: 44px; top: 150px; width: 318px; height: 336px;
    border-radius: 50%;
    background: linear-gradient(135deg,
      #f39a2b 0%,
      #4cab47 28%,
      #2fb3ae 48%,
      #2d9ad8 60%,
      #8e3f8f 76%,
      #d8306a 100%);
  }

  .cover__author {
    position: absolute; right: 41px; top: 14px;
    font-family: "Hind", sans-serif; font-weight: 400;
    font-size: 17px; color: var(--author-grey);
  }
  .cover__title {
    position: absolute; left: 33px; top: 34px;
    font-family: "Fira Sans Condensed", sans-serif; font-weight: 500;
    font-size: 44px; line-height: 1; letter-spacing: -0.5px;
  }
  .cover--balloons .cover__title { color: var(--title-magenta); }
  .cover--pilot .cover__title { color: var(--title-teal); top: 31px; }
  .cover--rainbow .cover__title { color: var(--title-plum); }

  .cover__subtitle {
    position: absolute; left: 35px; top: 85px;
    font-family: "Hind", sans-serif; font-weight: 500;
    color: var(--subtitle-grey); line-height: 0.95;
  }
  .cover--pilot .cover__subtitle { top: 81px; }
  .cover__subtitle-caps { display: block; font-size: 19px; letter-spacing: 0.3px; }
  .cover__subtitle-rest { display: block; font-size: 18px; }

  .cover__tagline {
    position: absolute; left: 35px; bottom: 14px;
    font-family: "Fira Sans", sans-serif; font-style: italic;
    font-size: 11.2px; line-height: 1.3;
  }
  .cover--balloons .cover__tagline { color: var(--title-magenta); }
  .cover--pilot .cover__tagline { color: var(--tag-grey); }
  .cover--rainbow .cover__tagline { color: var(--title-plum); }
</style>
</head>
<body>

<section class="cover cover--balloons">
  <div class="cover__art" role="img" aria-label="Comic-Zeichnung: Mädchen und kleines Kind schweben an bunten Luftballons davon"></div>
  <p class="cover__author">Henrike Molldorf</p>
  <h1 class="cover__title">Im stillen Garten</h1>
  <h2 class="cover__subtitle"><span class="cover__subtitle-caps">KONZENTRATIONSTRAINING</span><span class="cover__subtitle-rest">für Kinder in der Praxis</span></h2>
  <p class="cover__tagline">Die 39 besten Übungen für nachhaltig mehr Aufmerksamkeit<br>und Konzentration in der Schule und im Alltag</p>
</section>

<section class="cover cover--pilot">
  <div class="cover__art" role="img" aria-label="Aquarell-Comic: Junge mit Fliegermütze und Brille steht in einem türkisen Spielzeugflugzeug"></div>
  <p class="cover__author">Henrike Molldorf</p>
  <h1 class="cover__title">Im stillen Garten</h1>
  <h2 class="cover__subtitle"><span class="cover__subtitle-caps">KONZENTRATIONSTRAINING</span><span class="cover__subtitle-rest">für Kinder in der Praxis</span></h2>
  <p class="cover__tagline">Die 39 besten Übungen für nachhaltig mehr Aufmerksamkeit<br>und Konzentration in der Schule und im Alltag</p>
</section>

<section class="cover cover--rainbow">
  <div class="cover__art" role="img" aria-label="Weiße Silhouette eines springenden Kindes vor überlagerten Regenbogenkreisen mit bunten Punkten"></div>
  <p class="cover__author">Henrike Molldorf</p>
  <h1 class="cover__title">Im stillen Garten</h1>
  <h2 class="cover__subtitle"><span class="cover__subtitle-caps">KONZENTRATIONSTRAINING</span><span class="cover__subtitle-rest">für Kinder in der Praxis</span></h2>
  <p class="cover__tagline">Die 39 besten Übungen für nachhaltig mehr Aufmerksamkeit<br>und Konzentration in der Schule und im Alltag</p>
</section>

</body>
</html>
```